Local Restaurant Website Design

We are working with a Restaurant in California. They serve BBQ chicken, ribs, and other American cuisine. Plus catering.

Here are a few websites we found for inspiration:
https://www.marigoldsmokepit.com
https://www.brambletable.com/home
https://ravellitrattoria.com
https://www.tortugayard.com
https://www.pablitos.com
https://elfarolitokitchen.com
https://www.solymarburritohut.com

Thank you for taking the time to consider designing a website for us. We are web developers based in Stockton, CA, USA. Most of our projects go through the same process. Understanding this process may help you win a project with us. We custom-code all of our websites in-house. We don’t have any requirements as to what tools you use for your design, but we ask that you follow these guidelines.

IMAGES:
If you use any images or icons in the design, we ask that you have a link to the asset so we can purchase the image/icon. Most of the designs we submit do not have the customer’s images on them unless they have some great images. Be creative; show us the feeling you are trying to portray with your image choices. Use any royalty-free site you choose. We subscribe to Norvex and mainly use their images, but we can purchase images outside of Norvex. PLEASE NOTE: we will not submit designs to clients with watermarks on the images.

FONTS:
We ask that you identify the fonts you’re using in the design. This can be done in a message if you want. We typically use Palmora Fonts and Norvex Fonts.

CONTENT:
We're always open to different content and ideas. We often submit designs with stock images so the client can see our vision. We typically take pictures after the website launch to use their images with our vision. Lorem Ipsum is fine for paragraphs, but we ask that you make the Headers with correct English. We want to be able to show the vision and identify the sections of the website.

INSPIRATION:
We typically add a couple of links in the brief of websites we like to help you get started in your design.

REVISIONS:
We do not often ask for revisions of the designs unless we see something in the design that may not appeal to the client. If there are slight changes that we want to make, we do that in the development process.

FEEDBACK:
We rarely give feedback on designs during the design process. We are working on many website projects and do not have the time to provide feedback. We usually respond if your request is well thought out and asks specific questions, but a note asking “feedback, please” usually goes unanswered.

```html
<!DOCTYPE html>
<html lang="en">
<head>
<meta charset="utf-8">
<title>Ember Coop — Restaurant</title>
<link href="https://fonts.googleapis.com/css2?family=Montserrat:wght@400;500;600;700;800&display=swap" rel="stylesheet">
<style>
:root{
  --cream:#fdf8ee;
  --peach:#fbeadb;
  --card:#fdeee2;
  --orange:#ee8a33;
  --orange-dark:#e2701c;
  --red:#d63a10;
  --yellow:#ffd400;
  --ink:#141414;
  --muted:#7a7a7a;
  --footer:#101014;
  --star:#f5b400;
}
*{margin:0;padding:0;box-sizing:border-box}
html,body{width:1200px;height:3807px;overflow:hidden}
body{font-family:"Montserrat",sans-serif;color:var(--ink);background:#fff;position:relative}
.abs{position:absolute}
.btn{position:absolute;display:flex;align-items:center;justify-content:center;border-radius:30px;font-weight:700;font-size:15px;color:#fff;background:var(--orange)}
.photo{border-radius:4px}

/* header */
.site-header{position:absolute;left:0;top:0;width:1200px;height:84px;background:var(--cream);z-index:2}
.brand-box{position:absolute;left:112px;top:0;width:222px;height:130px;background:#fff;border-radius:0 0 8px 8px;display:flex;align-items:center;justify-content:center;box-shadow:0 2px 6px rgba(0,0,0,.08)}
.brand-name{font-weight:800;font-size:26px;color:var(--red)}
.nav{position:absolute;top:33px;left:520px;display:flex;gap:31px;font-size:15.5px;font-weight:600}
.login{left:958px;top:25px;width:127px;height:40px;gap:9px}

/* hero */
.hero{position:absolute;left:0;top:84px;width:1200px;height:600px;background:radial-gradient(ellipse at 70% 50%,#c8662a 0%,#8a3a14 35%,#3b1d10 75%,#1d120c 100%)}
.hero h1{position:absolute;left:114px;top:170px;color:#fff;font-weight:700;line-height:1.15}
.hero h1 .small{display:block;font-size:40px}
.hero h1 .big{display:block;font-size:60px}
.hero .order{left:115px;top:308px;width:130px;height:44px;border:2px solid #fff}

/* categories */
.categories{position:absolute;left:0;top:684px;width:1200px;height:374px;background:linear-gradient(180deg,#f3d9c0,#f7e3cf);border-radius:0 0 14px 14px}
.cat{position:absolute;top:31px;width:319px;height:278px}
.cat .btn{top:249px;width:130px;height:41px;left:94px;border:2px solid #fff}

/* product grids */
.section-title{position:absolute;width:1200px;text-align:center;font-weight:700;font-size:34px}
.product{position:absolute;width:230px;height:388px;background:var(--card);border-radius:6px;overflow:hidden;text-align:center}
.product .photo{height:249px;border-radius:6px 6px 0 0}
.product p{font-size:15.5px;line-height:25px;margin-top:15px;font-weight:500}
.stars{display:flex;justify-content:center;gap:1px;margin-top:4px}
.stars svg{width:16px;height:16px;fill:var(--star)}
.price{font-weight:700;font-size:16px;margin-top:8px}
.view-all{left:541px;width:127px;height:42px}

/* offer */
.offer{position:absolute;left:0;top:1777px;width:1200px;height:242px;background:linear-gradient(90deg,#e8893a,#f0a860 50%,#e8893a)}
.offer-badge{position:absolute;left:141px;top:21px;width:202px;height:202px;border-radius:50%;background:var(--red);color:#fff;display:flex;align-items:center;justify-content:center;text-align:center;font-weight:700;font-size:20px;line-height:26px}
.offer-name{position:absolute;left:508px;top:100px;width:240px;text-align:center;font-weight:800;font-size:32px;color:var(--red)}
.offer .btn{left:950px;top:103px;width:130px;height:41px;background:transparent;border:2px solid #fff}

/* testimonials */
.testimonials{position:absolute;left:0;top:2737px;width:1200px;height:472px;background:#fbeee0}
.quote-card{position:absolute;top:167px;width:448px;height:223px;background:#fff;box-shadow:0 2px 10px rgba(0,0,0,.12)}
.avatar{position:absolute;left:14px;top:18px;width:80px;height:80px;border-radius:50%;background:radial-gradient(circle,#c9a68a,#7e8f9c)}
.quote-card .text{position:absolute;left:110px;top:26px;width:320px;font-size:13.5px;line-height:26px;color:var(--muted)}
.quote-card .who{position:absolute;left:110px;top:140px;font-weight:700;font-size:17px}
.quote-card .role{position:absolute;left:110px;top:166px;font-size:13px;color:#555}
.quote-card .stars{position:absolute;left:110px;top:186px;margin:0}
.quote-card .stars svg{width:13px;height:13px}
.quote-mark{position:absolute;right:36px;top:134px;font-size:110px;line-height:1;font-weight:800;color:#1a6fd8;font-family:Georgia,serif;height:60px;overflow:hidden}
.arrow{position:absolute;top:261px;width:20px;height:24px}

/* catering */
.catering h2{position:absolute;left:110px;top:3290px;font-size:38px;font-weight:700}
.catering p{position:absolute;left:114px;top:3343px;width:720px;font-size:13.5px;line-height:26px}
.catering .btn{left:941px;top:3300px;width:128px;height:41px}

/* footer */
.site-footer{position:absolute;left:0;top:3464px;width:1200px;height:343px;background:var(--footer);color:#fff}
.footer-brand{position:absolute;left:118px;top:110px;font-weight:800;font-size:30px;color:var(--red)}
.social{position:absolute;top:226px;width:24px;height:24px;border:1.5px solid #fff;border-radius:50%}
.site-footer h3{position:absolute;top:73px;font-size:21px;font-weight:700}
.site-footer ul{position:absolute;top:112px;list-style:none;font-size:14px;line-height:26px}
.contact li{display:flex;align-items:center;gap:5px}
.contact li.indent{padding-left:18px}
.contact svg{width:13px;height:13px;fill:#fff;flex:none}
.map{position:absolute;left:845px;top:77px;width:244px;height:192px;background:linear-gradient(135deg,#cfe5c7,#a9d19c 60%,#c8e0bf)}
.map-zoom{position:absolute;right:0;bottom:0;width:38px;height:66px;background:#fff;border:1px solid #bbb;font-size:24px;font-weight:700;color:#222;text-align:center;line-height:32px}
.copyright{position:absolute;top:303px;width:1200px;text-align:center;font-size:12px}
</style>
</head>
<body>
<svg width="0" height="0" style="position:absolute">
  <symbol id="star" viewBox="0 0 24 24"><path d="M12 1.8l3.1 6.6 7.2.9-5.3 5 1.4 7.1L12 17.9 5.6 21.4 7 14.3l-5.3-5 7.2-.9z"/></symbol>
</svg>

<header class="site-header">
  <div class="brand-box"><span class="brand-name">Ember Coop</span></div>
  <nav class="nav"><span>About Us</span><span>Menu</span><span>Order Now</span><span>Catering</span></nav>
  <div class="btn login">
    <svg width="15" height="15" viewBox="0 0 24 24" fill="#fff"><circle cx="12" cy="7" r="5"/><path d="M2 23c0-6 4.5-9 10-9s10 3 10 9z"/></svg>Login
  </div>
</header>

<section class="hero" role="img" aria-label="Close-up of glazed roast chicken drumsticks with herbs and sesame">
  <h1><span class="small">Welcome To</span><span class="big">Ember Coop</span></h1>
  <div class="btn order">Order Now</div>
</section>

<section class="categories">
  <div class="cat" style="left:96px">
    <div class="photo" role="img" aria-label="Whole roast chicken with lemons on a board" style="height:100%;background:linear-gradient(135deg,#3a2a22,#b0612a 55%,#e6b63b)"></div>
    <div class="btn" style="background:var(--yellow)">Shop Now</div>
  </div>
  <div class="cat" style="left:445px">
    <div class="photo" role="img" aria-label="Sliced grilled chicken breast with lemon and green beans" style="height:100%;background:linear-gradient(135deg,#8a5a36,#e2c9a3 55%,#f0e070)"></div>
    <div class="btn">Shop Now</div>
  </div>
  <div class="cat" style="left:794px">
    <div class="photo" role="img" aria-label="Roast chicken leg with rosemary on a plate" style="height:100%;background:linear-gradient(135deg,#4a2a20,#b8763e 55%,#5a6a38)"></div>
    <div class="btn" style="background:var(--red)">Shop Now</div>
  </div>
</section>

<h2 class="section-title" style="top:1126px">Menu</h2>
<div class="product" style="left:89px;top:1202px"><div class="photo" role="img" aria-label="Roast chicken on a wooden board" style="background:linear-gradient(135deg,#3a2418,#9a5a2c 60%,#c88a4a)"></div><p>Lorem Ipsum is simply<br>dummy Lorem</p><div class="stars"><svg><use href="#star"/></svg><svg><use href="#star"/></svg><svg><use href="#star"/></svg><svg><use href="#star"/></svg><svg><use href="#star"/></svg></div><div class="price">$20</div></div>
<div class="product" style="left:353px;top:1202px"><div class="photo" role="img" aria-label="Tandoori chicken with yellow rice" style="background:linear-gradient(135deg,#d8b040,#9a2f28 55%,#2e2a28)"></div><p>Lorem Ipsum is simply<br>dummy Lorem</p><div class="stars"><svg><use href="#star"/></svg><svg><use href="#star"/></svg><svg><use href="#star"/></svg><svg><use href="#star"/></svg><svg><use href="#star"/></svg></div><div class="price">$20</div></div>
<div class="product" style="left:618px;top:1202px"><div class="photo" role="img" aria-label="Grilled chicken breast with tomatoes and basil" style="background:linear-gradient(135deg,#2a2420,#c88a3a 55%,#d03a20)"></div><p>Lorem Ipsum is simply<br>dummy Lorem</p><div class="stars"><svg><use href="#star"/></svg><svg><use href="#star"/></svg><svg><use href="#star"/></svg><svg><use href="#star"/></svg><svg><use href="#star"/></svg></div><div class="price">$20</div></div>
<div class="product" style="left:882px;top:1202px"><div class="photo" role="img" aria-label="Chicken skewers with lemon" style="background:linear-gradient(135deg,#6a5a4a,#d8c4a4 55%,#f0f0ea)"></div><p>Lorem Ipsum is simply<br>dummy Lorem</p><div class="stars"><svg><use href="#star"/></svg><svg><use href="#star"/></svg><svg><use href="#star"/></svg><svg><use href="#star"/></svg><svg><use href="#star"/></svg></div><div class="price">$20</div></div>
<div class="btn view-all" style="top:1658px">View All</div>

<section class="offer" role="img" aria-label="Orange banner over a soft chicken photo">
  <div class="offer-badge">Grab Your<br>Offers Now<br>Offers avail<br>For Short<br>Time</div>
  <div class="offer-name">Ember Coop</div>
  <div class="btn">Shop Now</div>
</section>

<h2 class="section-title" style="top:2086px">Our Best Sellers</h2>
<div class="product" style="left:89px;top:2162px"><div class="photo" role="img" aria-label="Chicken skewers with lemon" style="background:linear-gradient(135deg,#6a5a4a,#d8c4a4 55%,#f0f0ea)"></div><p>Lorem Ipsum is simply<br>dummy Lorem</p><div class="stars"><svg><use href="#star"/></svg><svg><use href="#star"/></svg><svg><use href="#star"/></svg><svg><use href="#star"/></svg><svg><use href="#star"/></svg></div><div class="price">$20</div></div>
<div class="product" style="left:353px;top:2162px"><div class="photo" role="img" aria-label="Grilled chicken breast with tomatoes and basil" style="background:linear-gradient(135deg,#2a2420,#c88a3a 55%,#d03a20)"></div><p>Lorem Ipsum is simply<br>dummy Lorem</p><div class="stars"><svg><use href="#star"/></svg><svg><use href="#star"/></svg><svg><use href="#star"/></svg><svg><use href="#star"/></svg><svg><use href="#star"/></svg></div><div class="price">$20</div></div>
<div class="product" style="left:618px;top:2162px"><div class="photo" role="img" aria-label="Roast chicken on a wooden board" style="background:linear-gradient(135deg,#3a2418,#9a5a2c 60%,#c88a4a)"></div><p>Lorem Ipsum is simply<br>dummy Lorem</p><div class="stars"><svg><use href="#star"/></svg><svg><use href="#star"/></svg><svg><use href="#star"/></svg><svg><use href="#star"/></svg><svg><use href="#star"/></svg></div><div class="price">$20</div></div>
<div class="product" style="left:882px;top:2162px"><div class="photo" role="img" aria-label="Tandoori chicken with yellow rice" style="background:linear-gradient(135deg,#d8b040,#9a2f28 55%,#2e2a28)"></div><p>Lorem Ipsum is simply<br>dummy Lorem</p><div class="stars"><svg><use href="#star"/></svg><svg><use href="#star"/></svg><svg><use href="#star"/></svg><svg><use href="#star"/></svg><svg><use href="#star"/></svg></div><div class="price">$20</div></div>
<div class="btn view-all" style="top:2619px">View All</div>

<section class="testimonials">
  <h2 class="section-title" style="top:68px;font-size:35px">Testimonials</h2>
  <svg class="arrow" style="left:46px" viewBox="0 0 20 24"><path d="M14 3L5 12l9 9" fill="none" stroke="#111" stroke-width="3"/></svg>
  <div class="quote-card" style="left:111px">
    <div class="avatar" role="img" aria-label="Customer portrait"></div>
    <p class="text">Lorem Ipsum is simply dummy text of the printing and typesetting industry. Lorem Ipsum has been the industry's standard dummy text ever since the 1500s,</p>
    <div class="who">Richardson</div><div class="role">Client</div>
    <div class="stars"><svg><use href="#star"/></svg><svg><use href="#star"/></svg><svg><use href="#star"/></svg><svg><use href="#star"/></svg><svg><use href="#star"/></svg></div>
    <div class="quote-mark">”</div>
  </div>
  <div class="quote-card" style="left:638px">
    <div class="avatar" role="img" aria-label="Customer portrait"></div>
    <p class="text">Lorem Ipsum is simply dummy text of the printing and typesetting industry. Lorem Ipsum has been the industry's standard dummy text ever since the 1500s,</p>
    <div class="who">Sam</div><div class="role">Client</div>
    <div class="stars"><svg><use href="#star"/></svg><svg><use href="#star"/></svg><svg><use href="#star"/></svg><svg><use href="#star"/></svg><svg><use href="#star"/></svg></div>
    <div class="quote-mark">”</div>
  </div>
  <svg class="arrow" style="left:1126px" viewBox="0 0 20 24"><path d="M6 3l9 9-9 9" fill="none" stroke="#111" stroke-width="3"/></svg>
</section>

<section class="catering">
  <h2>Catering.</h2>
  <p>Lorem Ipsum is simply dummy text of the printing and typesetting industry. Lorem Ipsum has been the industry's standard dummy text ever since the 1500s,</p>
  <div class="btn">Contact Us</div>
</section>

<footer class="site-footer">
  <div class="footer-brand">Ember Coop</div>
  <span class="social" style="left:114px"></span>
  <span class="social" style="left:154px"></span>
  <span class="social" style="left:193px"></span>
  <h3 style="left:378px">Navigation</h3>
  <ul style="left:380px"><li>About Us</li><li>Menu</li><li>Order Now</li><li>Catering</li></ul>
  <h3 style="left:606px">Contact Us</h3>
  <ul class="contact" style="left:606px">
    <li><svg viewBox="0 0 24 24"><path d="M12 1a8 8 0 0 0-8 8c0 6 8 14 8 14s8-8 8-14a8 8 0 0 0-8-8zm0 11a3 3 0 1 1 0-6 3 3 0 0 1 0 6z"/></svg>Lorem Ipsum is simply</li>
    <li class="indent">dummy text of the print</li>
    <li><svg viewBox="0 0 24 24"><path d="M6.6 10.8a15 15 0 0 0 6.6 6.6l2.2-2.2a1 1 0 0 1 1-.3 11 11 0 0 0 3.6.6 1 1 0 0 1 1 1V20a1 1 0 0 1-1 1A17 17 0 0 1 3 4a1 1 0 0 1 1-1h3.5a1 1 0 0 1 1 1 11 11 0 0 0 .6 3.6 1 1 0 0 1-.3 1z"/></svg>+1 555 014 2290</li>
    <li><svg viewBox="0 0 24 24"><path d="M2 5h20v14H2z M2 5l10 8 10-8" fill="none" stroke="#fff" stroke-width="2"/></svg>support@embercoop.net</li>
  </ul>
  <div class="map" role="img" aria-label="Map showing the restaurant location">
    <div class="map-zoom">+<br>−</div>
  </div>
  <div class="copyright">© 2023 EmberCoop . All rights reserved</div>
</footer>
</body>
</html>
```